Animal Eye Clinic needs a Business card

We are a new veterinary ophthalmology practice (Tessaly Animal Eye Care) and we need a business card designed. We only see animal eyes - we are not a regular veterinary clinic. We already have a logo. We are looking for a professional, good looking business card to hand out to our clients. We are looking for something simple but professional and contemporary. Our logo is likely the only picture/graphic that needs to be on the card.
Updates

Contact Information for Business Card

Marisol Dunkley, BSc, DVM, MSc, DipACVO
Veterinary Ophthalmologist

Phone: 555.418.3097
Email: tessalyanimaleyecare@mailbrook.net
Website: tessalyanimaleyecare.net
Address: 1840 Pellworth Rd
Harrowfield, NS, V4T 8M3

Colors

Designer to choose colors to be used in the design.

Requirements
Must have
• Our logo (attached)

```html
<!DOCTYPE html>
<html lang="en">
<head>
<meta charset="utf-8">
<title>Tessaly Animal Eye Care – Business Card</title>
<link rel="stylesheet" href="https://fonts.googleapis.com/css2?family=Open+Sans:wght@400;600;700&display=swap">
<style>
  :root {
    --teal: #0396a6;
    --white: #ffffff;
    --ink: #1d1d1f;
    --muted: #6b6d70;
    --backdrop: #e6e7e8;
    --card-w: 474px;
    --card-h: 269px;
  }
  * { box-sizing: border-box; margin: 0; padding: 0; }
  html, body {
    width: 1200px;
    height: 1200px;
    overflow: hidden;
    background: var(--backdrop);
    font-family: "Open Sans", Arial, sans-serif;
  }
  .card {
    position: absolute;
    left: 356px;
    width: var(--card-w);
    height: var(--card-h);
    overflow: hidden;
    background: var(--white);
  }
  .card--front { top: 151px; }
  .card--back { top: 748px; }
  .card__shape {
    position: absolute;
    inset: 0;
    width: 100%;
    height: 100%;
  }

  .brand {
    position: absolute;
    left: 75px;
    top: 100px;
    display: flex;
    align-items: center;
    gap: 16px;
  }
  .brand__dot {
    width: 58px;
    height: 58px;
    border-radius: 50%;
    background: var(--teal);
    flex: none;
  }
  .brand__name {
    color: var(--teal);
    font-weight: 700;
    font-size: 21px;
    line-height: 1.1;
    text-transform: uppercase;
    letter-spacing: 0.2px;
  }

  .practitioner {
    position: absolute;
    right: 74px;
    top: 222px;
    text-align: right;
  }
  .practitioner__name {
    font-size: 10.5px;
    font-weight: 600;
    color: var(--ink);
    line-height: 16px;
    white-space: nowrap;
  }
  .practitioner__role {
    font-size: 10.5px;
    color: var(--muted);
    line-height: 16px;
  }

  .back-mark {
    position: absolute;
    left: 92px;
    top: 112px;
    width: 52px;
    height: 52px;
    border-radius: 50%;
    background: var(--white);
  }
  .divider {
    position: absolute;
    left: 176px;
    top: 99px;
    width: 1.5px;
    height: 77px;
    background: var(--white);
  }
  .contact {
    position: absolute;
    left: 186px;
    top: 96px;
    list-style: none;
    color: var(--white);
    font-size: 10.5px;
    line-height: 16.5px;
    white-space: nowrap;
  }
</style>
</head>
<body>

  <section class="card card--front" aria-label="Business card front">
    <svg class="card__shape" viewBox="0 0 474 269" preserveAspectRatio="none" aria-hidden="true">
      <defs>
        <filter id="edge-shadow" x="-10%" y="-10%" width="120%" height="120%">
          <feDropShadow dx="-2" dy="0" stdDeviation="3" flood-color="#000" flood-opacity="0.25"/>
        </filter>
      </defs>
      <rect width="474" height="269" fill="var(--teal)"/>
      <path d="M244 0 C120 22 40 82 15 134.5 C40 187 120 247 244 269 L474 269 L474 0 Z"
            fill="var(--white)" filter="url(#edge-shadow)"/>
    </svg>

    <div class="brand">
      <span class="brand__dot"></span>
      <span class="brand__name">Tessaly<br>Animal Eye Care</span>
    </div>

    <div class="practitioner">
      <p class="practitioner__name">Marisol Dunkley, BSc, DVM, MSc, DipACVO</p>
      <p class="practitioner__role">Veterinary Ophthalmologist</p>
    </div>
  </section>

  <section class="card card--back" aria-label="Business card back">
    <svg class="card__shape" viewBox="0 0 474 269" preserveAspectRatio="none" aria-hidden="true">
      <defs>
        <filter id="edge-shadow-back" x="-10%" y="-10%" width="120%" height="120%">
          <feDropShadow dx="-2" dy="0" stdDeviation="3" flood-color="#000" flood-opacity="0.25"/>
        </filter>
      </defs>
      <rect width="474" height="269" fill="var(--white)"/>
      <path d="M244 0 C120 22 40 82 15 134.5 C40 187 120 247 244 269 L474 269 L474 0 Z"
            fill="var(--teal)" filter="url(#edge-shadow-back)"/>
    </svg>

    <span class="back-mark"></span>
    <span class="divider"></span>
    <ul class="contact">
      <li>Phone: 555.418.3097</li>
      <li>Email: tessalyanimaleyecare@mailbrook.net</li>
      <li>Website: tessalyanimaleyecare.net</li>
      <li>Address: 1840 Pellworth Rd</li>
      <li>Harrowfield, NS, V4T 8M3</li>
    </ul>
  </section>

</body>
</html>
```